bright lane coaching needs snazzy business card that serves a dual purpose

business card needed for a Bright Lane Coaching company that takes people out on the road to teach them proficiency on their bike.
My business logo is attached. I have grey and aqua colours with my logo.
i really like bitumen/tarmac/ road in the design somehow but that is up to you.
I think navy blue will go well with my colours too. see how you go.

I want this card to look REALLY good.
the back of the card may be used for emergency contact details too
In case of Emergency I am:
Name:

Emergency Contact name
emergency contact Phone number:

• details that are essential are:
• logo
• Name: Marnie HOLT
• ABN: 53 916 204 871
• phone number: 0438 152 964
• facebook logo
• * ride tuition & proficiency
• * skills practice
• * maintenance 101
• * bike fitting service
• * cater for all ages & abilities
• backpage:
• logo
• skills confidence enjoyment
• some space for writing
• nothing girly. The business will already naturally attract women, it needs to appeal to both genders

```html
<!DOCTYPE html>
<html lang="en">
<head>
<meta charset="utf-8">
<title>Bright Lane Coaching – Business Card</title>
<link href="https://fonts.googleapis.com/css2?family=Lato:wght@300;400;700;900&display=swap" rel="stylesheet">
<style>
  :root {
    --aqua: #4fbcae;
    --aqua-light: #6fcfc2;
    --aqua-dark: #3aa697;
    --grey: #4a4d50;
    --grey-mid: #8a8d90;
    --grey-light: #c9cbcc;
    --paper: #fbfbfb;
    --backdrop: #ecebe8;
    --road-light: #9ea2a4;
    --road-dark: #4f5457;
    --road-verge: #d9d6c9;
  }
  * { margin: 0; padding: 0; box-sizing: border-box; }
  html, body { width: 1200px; height: 1023px; overflow: hidden; }
  body {
    background: var(--backdrop);
    font-family: "Lato", Arial, sans-serif;
    color: var(--grey);
    position: relative;
  }
  .card {
    position: absolute;
    left: 280px;
    width: 640px;
    height: 366px;
    border-radius: 22px;
    overflow: hidden;
    background: var(--paper);
    box-shadow: 0 10px 28px rgba(0,0,0,0.18);
  }
  .card--front { top: 90px; }
  .card--back { top: 566px; }

  /* Front */
  .road {
    position: absolute; inset: 0;
    background: linear-gradient(135deg, var(--road-light) 0%, #7d8285 45%, var(--road-dark) 100%);
    clip-path: polygon(62% 0, 100% 0, 100% 100%, 100% 100%);
  }
  .road-edge {
    position: absolute; inset: 0;
    background: var(--road-verge);
    clip-path: polygon(61.3% 0, 62% 0, 100% 100%, 99.2% 100%);
  }
  .brand {
    position: absolute; left: 40px; top: 34px;
    display: flex; align-items: center; gap: 14px;
  }
  .brand-dot {
    width: 22px; height: 22px; border-radius: 50%;
    background: var(--aqua);
    flex: none;
  }
  .brand-name {
    font-weight: 300; font-size: 30px; letter-spacing: 1px;
    color: var(--grey); text-transform: uppercase; line-height: 1.08;
  }
  .brand-name span { display: block; }
  .rule {
    position: absolute; left: 40px; top: 108px;
    width: 300px; height: 1px; background: var(--grey-mid);
  }
  .person {
    position: absolute; left: 40px; top: 116px;
    font-weight: 900; font-size: 24px; color: var(--aqua);
  }
  .abn {
    position: absolute; left: 40px; top: 150px;
    font-size: 15px; color: var(--grey);
  }
  .phone {
    position: absolute; left: 40px; top: 174px;
    display: flex; align-items: center; gap: 12px;
    font-size: 32px; font-weight: 400; color: var(--grey);
  }
  .phone svg { width: 28px; height: 28px; }
  .services {
    position: absolute; left: 40px; top: 226px;
    list-style: none; font-size: 16px; line-height: 23px; color: var(--grey);
  }
  .services li { display: flex; align-items: center; gap: 10px; }
  .services li::before {
    content: ""; width: 8px; height: 8px; border-radius: 50%;
    border: 1.5px solid var(--grey-mid);
  }

  /* Back */
  .back-shape { position: absolute; inset: 0; width: 100%; height: 100%; }
  .back-brand {
    position: absolute; right: 40px; top: 48px; text-align: right;
  }
  .back-brand .brand-name { color: #fff; font-size: 36px; }
  .tagline {
    margin-top: 8px; font-size: 18px; font-weight: 300;
    color: #fff; letter-spacing: 0.5px;
  }
  .notes {
    position: absolute; left: 90px; top: 250px;
    font-weight: 700; font-size: 18px; color: var(--grey);
  }
  .emergency {
    position: absolute; right: 40px; top: 196px;
    color: #fff; font-weight: 700; text-align: right;
  }
  .emergency h2 { font-size: 22px; font-weight: 900; margin-bottom: 6px; }
  .emergency p { font-size: 18px; line-height: 26px; }
  .emergency span { font-weight: 400; }
</style>
</head>
<body>

<section class="card card--front">
  <div class="road" role="img" aria-label="Photograph of a tarmac road surface"></div>
  <div class="road-edge"></div>
  <div class="brand">
    <span class="brand-dot"></span>
    <div class="brand-name"><span>Bright Lane</span><span>Coaching</span></div>
  </div>
  <div class="rule"></div>
  <div class="person">Marnie HOLT</div>
  <div class="abn">ABN: 53 916 204 871</div>
  <div class="phone">
    <svg viewBox="0 0 24 24" aria-hidden="true"><path fill="#8a8d90" d="M6.6 10.8a15.1 15.1 0 0 0 6.6 6.6l2.2-2.2a1 1 0 0 1 1-.25 11.4 11.4 0 0 0 3.6.57 1 1 0 0 1 1 1V20a1 1 0 0 1-1 1A17 17 0 0 1 3 4a1 1 0 0 1 1-1h3.5a1 1 0 0 1 1 1c0 1.25.2 2.45.57 3.57a1 1 0 0 1-.25 1z"/></svg>
    <span>0438 152 964</span>
  </div>
  <ul class="services">
    <li>ride tuition &amp; proficiency</li>
    <li>skills practice</li>
    <li>maintenance 101</li>
    <li>bike fitting service</li>
    <li>cater for all ages &amp; abilities</li>
  </ul>
</section>

<section class="card card--back">
  <svg class="back-shape" viewBox="0 0 640 366" preserveAspectRatio="none" aria-hidden="true">
    <rect width="640" height="366" fill="var(--aqua)"/>
    <path d="M0 80 C 180 90, 330 180, 400 366 L 0 366 Z" fill="var(--paper)"/>
  </svg>
  <div class="back-brand">
    <div class="brand-name">Bright Lane Coaching</div>
    <div class="tagline">skills confidence enjoyment</div>
  </div>
  <div class="notes">Notes Here</div>
  <div class="emergency">
    <h2>In case of Emergency</h2>
    <p>Name: <span>Dale Porter</span></p>
    <p>Phone: <span>53 916 204 871</span></p>
  </div>
</section>

</body>
</html>
```